Direct Mail Postcard for a preschool

We need a direct mail postcard to market our dual language program at our preschool. The postcard size is 8.5 x 5.5 inches and we will need something that prints on both the front and the back. Our dual language program is for four year olds and provides training in Spanish and English. Education for four year olds in Florida is paid for by the state. I had a direct mail company create a card, which I didn't like at all. I am enclosing that card as one of the uploaded files for your review. The final design should communicate safety and our ability to teach four year olds both languages and to provide general education. We service an affluent community who value education. Our teacher has great credentials. She has an elementary education bachelors and a teaching certificate endorsement in Spanish language. Our school is one of the largest facilities in the area. It is a four acre campus with lush landscaping, several playgrounds, two pools and a large school building. I would like to also stress our location, as some people may not realize exactly where the school is located. Our website is www.brightmeadowlearning.net. I have included optional pictures which could be used in this postcard.
Updates

The text in the original post card is not required to be in your submission. Feel free to change it if you feel there is a better way to deliver the dual language class message. I created the primary line "It's never too early to learn a second language". The other two headings ("creating environments where all children learn while having fun" and "every child deserves quality time") were both invented by the previous design company. 

Target Market(s)

Moms with four year old children will often be the target decision maker. Most are affluent parents who value education and a dual language training.

Industry/Entity Type

Preschool

Requirements
Must have
• Our logo must be used. However, the school's name is Sunny Acorns at Harrowgate. This is different from the other Sunny Acorns schools, so I would like to stress the at Harrowgate part. I would like to stress academics.
Should not have
• I don't want a design that includes cartoon figures. I like to use pictures of actual happy children.

```html
<!DOCTYPE html>
<html lang="en">
<head>
<meta charset="utf-8">
<title>Sunny Acorns at Harrowgate – Dual Language Postcard</title>
<link rel="stylesheet" href="https://fonts.googleapis.com/css2?family=Arimo:wght@400;700&family=Open+Sans:wght@600&family=Delius&family=Tinos&display=swap">
<style>
  :root {
    --page-bg: #e8e5e0;
    --front-teal: #bfe3e0;
    --front-mist: #eef6f4;
    --headline-orange: #f08a1c;
    --ink: #1e1e1e;
    --ink-soft: #3a3a3a;
    --bullet-blue: #2a86c8;
    --button-blue: #8fd0f2;
    --button-ink: #124a7a;
    --strip-white: #ffffff;
    --url-grey: #555555;
    --back-top: #ffffff;
    --back-bottom: #d9d9d9;
    --quote-ink: #3b3b3b;
    --motto-purple: #4b3f8f;
    --band-teal: #3ecfb2;
    --address-ink: #555555;
  }
  * { box-sizing: border-box; margin: 0; padding: 0; }
  html, body { width: 1200px; height: 750px; overflow: hidden; }
  body { background: var(--page-bg); position: relative; font-family: "Arimo", Arial, sans-serif; }

  .postcard {
    position: absolute; top: 194px; width: 560px; height: 362px; overflow: hidden;
    box-shadow: 0 2px 10px rgba(0,0,0,.18);
  }
  .postcard--front { left: 30px; background: radial-gradient(circle at 75% 30%, var(--front-mist) 0%, var(--front-teal) 75%); }
  .postcard--back { left: 610px; background: linear-gradient(180deg, var(--back-top) 0%, var(--back-bottom) 100%); }

  .postcard--front > * { z-index: 2; }
  .postcard--front > .front-photo { z-index: 1; }

  /* Front */
  .brand { position: absolute; left: 14px; top: 22px; display: flex; align-items: center; gap: 5px; width: 104px; }
  .brand__dot { width: 14px; height: 14px; border-radius: 50%; background: var(--headline-orange); flex: none; }
  .brand__name { font-family: "Delius", cursive; font-size: 15px; line-height: 1.05; color: var(--headline-orange); }
  .headline { position: absolute; left: 120px; top: 26px; width: 430px; font-family: "Delius", cursive; font-weight: 400; font-size: 18px; color: var(--headline-orange); white-space: nowrap; }
  .offer { position: absolute; left: 16px; top: 102px; font-size: 8.6px; font-weight: 700; color: var(--ink); }
  .benefits { position: absolute; left: 10px; top: 130px; width: 230px; list-style: none; font-size: 7.6px; line-height: 1.5; color: var(--ink-soft); }
  .benefits li { position: relative; padding-left: 10px; margin-bottom: 7px; }
  .benefits li::before { content: ""; position: absolute; left: 0; top: 3.5px; width: 4.5px; height: 4.5px; border-radius: 50%; background: var(--bullet-blue); }
  .call { position: absolute; left: 10px; top: 214px; width: 190px; text-align: center; font-size: 14.5px; font-weight: 700; line-height: 1.4; color: var(--ink); }
  .phone-button { position: absolute; left: 66px; top: 263px; width: 78px; height: 22px; border-radius: 3px; background: var(--button-blue); color: var(--button-ink); font-size: 8.6px; display: flex; align-items: center; justify-content: center; }
  .front-photo { position: absolute; left: 220px; top: 70px; width: 340px; height: 270px; background: radial-gradient(ellipse at 65% 45%, #e9cfa8 0%, #d8c6a4 35%, rgba(191,227,224,0) 72%); }
  .front-strip { position: absolute; left: 0; bottom: 0; width: 100%; height: 22px; background: var(--strip-white); display: flex; align-items: center; justify-content: flex-end; padding-right: 16px; font-size: 9.4px; color: var(--url-grey); }

  /* Back */
  .back-photo { position: absolute; left: 0; top: 0; width: 372px; height: 236px; background: radial-gradient(ellipse at 40% 50%, #b9a0c8 0%, #d8cfc2 40%, rgba(255,255,255,0) 75%); }
  .map { position: absolute; left: 386px; top: 20px; width: 168px; height: 118px; background: #d8d6cc; border: 1px solid #c4c2b8; }
  .address { position: absolute; left: 388px; top: 148px; font-family: "Tinos", serif; font-size: 9.4px; line-height: 1.68; color: var(--address-ink); font-style: normal; }
  .quote { position: absolute; left: 0; top: 258px; width: 100%; text-align: center; font-family: "Open Sans", sans-serif; font-weight: 600; font-size: 15px; color: var(--quote-ink); }
  .quote__mark { position: absolute; top: -14px; font-family: Georgia, serif; font-size: 30px; color: var(--ink); }
  .quote__mark--open { left: 26px; }
  .quote__mark--close { right: 14px; }
  .motto { position: absolute; left: 0; top: 296px; width: 100%; text-align: center; font-family: "Delius", cursive; font-size: 14px; color: var(--motto-purple); }
  .contact-band { position: absolute; left: 0; bottom: 0; width: 100%; height: 22px; background: var(--band-teal); display: flex; align-items: center; padding-left: 16px; font-size: 10px; font-weight: 700; color: #fff; }
  .contact-band__divider { width: 1px; height: 14px; background: rgba(255,255,255,.7); margin: 0 16px; }
</style>
</head>
<body>

<section class="postcard postcard--front" aria-label="Postcard front">
  <div class="front-photo" role="img" aria-label="Photo of a smiling preschool girl resting her chin on her hands beside a sketched stack of books and a pencil"></div>
  <div class="brand"><span class="brand__dot"></span><span class="brand__name">Sunny Acorns</span></div>
  <h1 class="headline">It's never too early to learn a second language</h1>
  <p class="offer">Enroll Your 4-year-old in our English/Spanish dual language VPK program</p>
  <ul class="benefits">
    <li>Classes start in August and September</li>
    <li>Enroll today at Sunny Acorns at Harrowgate,located on our beautiful 4-acre campus at Larkfield and Cedar Road</li>
    <li>Receive funding from the State of Florida for VPK tuition</li>
  </ul>
  <p class="call">Call today to schedule<br>a private tour</p>
  <div class="phone-button">(555) 014-2087</div>
  <div class="front-strip">www.brightmeadowlearning.net</div>
</section>

<section class="postcard postcard--back" aria-label="Postcard back">
  <div class="back-photo" role="img" aria-label="Photo of three young children lying on the floor drawing on paper"></div>
  <div class="map" role="img" aria-label="Street map showing the school location"></div>
  <address class="address">Sunny Acorns<br>4820 Larkfield Road<br>Larkfield, FL 33099</address>
  <p class="quote"><span class="quote__mark quote__mark--open">“</span>Creating environments where all children learn while having fun!<span class="quote__mark quote__mark--close">”</span></p>
  <p class="motto">Every Child Deserves Quality Time</p>
  <div class="contact-band">
    <span>www.brightmeadowlearning.com</span>
    <span class="contact-band__divider"></span>
    <span>(555) 014-2087</span>
  </div>
</section>

</body>
</html>
```